Business Card Design for Portrait photography professional

We are a small company specializing in portrait photography (weddings, family, couples, children, newborn, pregnant, etc.) Occasionally we do business portraits too and do some other type of photography. We need a business card which would fit into the same look and feel as our website theme (lumvira.com - under construction currently).
Our target customer base lies within mid- to upmarket. We want our business cards to convey a feeling of quality, solidness and a bit luxury.
Design should be universal and usable on 85mmx55mm, 90mmx50mm and 90mmx55mm
one extra file (PSD of a website didn't fit into the allowed updoad, therefore has put it into my dropbox: https://www.filqueso.com/s/qt8wr3kadhy5lbv/website%20theme%20PSD.psd)

Target Market(s)

mostly private people, 25-60 years old, mostly well established.

Industry/Entity Type

Portrait Photography

Requirements
Must have
• 2 sided design (print on both sides of the business card).
Must include:
business name, logo, URL (lumvira.no) , employee name, email address, and phone number.
Colorscheme of the website lumvira.no / lumvira.com

```html
<!DOCTYPE html>
<html lang="en">
<head>
<meta charset="utf-8">
<title>Lumvira – Business Card</title>
<link rel="stylesheet" href="https://fonts.googleapis.com/css2?family=Crimson+Text:wght@400;600&display=swap">
<style>
  :root {
    --canvas: #1c1c1c;
    --card: #000000;
    --band-light: #4a4a4a;
    --band-mid: #262626;
    --ink: #ffffff;
    --ink-soft: #d9d9d9;
    --rule: #5a5a5a;
  }
  * { box-sizing: border-box; margin: 0; padding: 0; }
  html, body { width: 1112px; height: 1200px; overflow: hidden; }
  body {
    background: var(--canvas);
    font-family: "Crimson Text", Georgia, serif;
    color: var(--ink);
    position: relative;
  }
  .card {
    position: absolute;
    left: 106px;
    width: 900px;
    height: 500px;
    background: var(--card);
    overflow: hidden;
  }
  .card--back { top: 70px; }
  .card--front { top: 630px; }
  .band {
    position: absolute;
    left: 0; right: 0;
    height: 46px;
    background: radial-gradient(ellipse 55% 160% at 50% 50%, var(--band-light), var(--band-mid) 60%, #0d0d0d 100%);
  }
  .band--top { top: 0; }
  .band--bottom { bottom: 0; }
  .brand {
    position: absolute;
    display: flex;
    align-items: center;
    gap: 16px;
    color: var(--ink);
    font-weight: 600;
  }
  .brand__dot {
    border: 3px solid var(--ink);
    border-radius: 50%;
    flex: none;
  }
  .card--back .brand {
    left: 50%; top: 50%;
    transform: translate(-50%, -50%);
    font-size: 64px;
    letter-spacing: 2px;
  }
  .card--back .brand__dot { width: 40px; height: 40px; }
  .card--front .brand {
    left: 86px; top: 116px;
    font-size: 40px;
    letter-spacing: 1px;
  }
  .card--front .brand__dot { width: 26px; height: 26px; }
  .identity {
    position: absolute;
    right: 110px;
    top: 140px;
    text-align: right;
  }
  .identity__name {
    font-size: 40px;
    font-weight: 600;
    line-height: 1;
    padding-bottom: 8px;
    background: linear-gradient(to right, transparent, var(--rule) 40%, var(--rule) 70%, transparent) bottom / 100% 1px no-repeat;
  }
  .identity__role {
    font-size: 21px;
    color: var(--ink-soft);
    margin-top: 6px;
  }
  .contacts {
    position: absolute;
    left: 505px;
    top: 296px;
    list-style: none;
  }
  .contacts__item {
    display: flex;
    align-items: center;
    gap: 16px;
    height: 46px;
    font-size: 22px;
    background: linear-gradient(to right, transparent, #3a3a3a 30%, transparent 75%) bottom / 100% 1px no-repeat;
  }
  .contacts__icon { width: 26px; height: 26px; flex: none; }
</style>
</head>
<body>

  <section class="card card--back" aria-label="Card back">
    <div class="band band--top"></div>
    <div class="brand"><span class="brand__dot"></span>Lumvira</div>
    <div class="band band--bottom"></div>
  </section>

  <section class="card card--front" aria-label="Card front">
    <div class="band band--top"></div>

    <div class="brand"><span class="brand__dot"></span>Lumvira</div>

    <div class="identity">
      <div class="identity__name">Your Name Here</div>
      <div class="identity__role">Photographer</div>
    </div>

    <ul class="contacts">
      <li class="contacts__item">
        <svg class="contacts__icon" viewBox="0 0 26 26" aria-hidden="true">
          <rect x="1.5" y="1.5" width="23" height="23" rx="6" fill="none" stroke="#fff" stroke-width="2"/>
          <path d="M8 7c-1 2 0 7 4 10s6 3 7 2l-2-3-2 1c-2-1-3-3-4-5l1-2z" fill="#fff"/>
        </svg>
        <span>0917.555.012</span>
      </li>
      <li class="contacts__item">
        <svg class="contacts__icon" viewBox="0 0 26 26" aria-hidden="true">
          <rect x="1.5" y="1.5" width="23" height="23" rx="6" fill="none" stroke="#fff" stroke-width="2"/>
          <rect x="6" y="8" width="14" height="10" fill="none" stroke="#fff" stroke-width="1.6"/>
          <path d="M6 8l7 6 7-6M6 18l5-5M20 18l-5-5" fill="none" stroke="#fff" stroke-width="1.4"/>
        </svg>
        <span>your_email@mailnest.com</span>
      </li>
      <li class="contacts__item">
        <svg class="contacts__icon" viewBox="0 0 26 26" aria-hidden="true">
          <rect x="1.5" y="1.5" width="23" height="23" rx="6" fill="none" stroke="#fff" stroke-width="2"/>
          <circle cx="13" cy="13" r="7" fill="none" stroke="#fff" stroke-width="1.6"/>
          <ellipse cx="13" cy="13" rx="3" ry="7" fill="none" stroke="#fff" stroke-width="1.2"/>
          <path d="M6 13h14M7.5 9.5h11M7.5 16.5h11" stroke="#fff" stroke-width="1.2"/>
        </svg>
        <span>www.lumvira.com</span>
      </li>
    </ul>

    <div class="band band--bottom"></div>
  </section>

</body>
</html>
```